Tellwick Asset Management - Corporate Letter Head Project

Looking for a classy design based on our current logo. Please find current logo source file in files. With our color scheme.

Target Market(s)

We're an investment firm, the letterhead needs to look professional and attractive to clients.

Industry/Entity Type

Hedgefund

Colors
0054AA
0677BA
7BADD7
CADEEF
E8F1F8

Requirements
Must have
• Our logo, address, phone number, and email

```html
<!DOCTYPE html>
<html lang="en">
<head>
<meta charset="utf-8">
<title>Tellwick Asset Management – Letterhead</title>
<link href="https://fonts.googleapis.com/css2?family=Arimo:wght@400;700&display=swap" rel="stylesheet">
<style>
  :root {
    --paper: #e7e7e9;
    --ink: #3b3b3d;
    --navy: #0c1729;
    --rule: #0c1729;
  }
  * { margin: 0; padding: 0; box-sizing: border-box; }
  html, body { width: 950px; height: 1200px; overflow: hidden; }
  body { background: var(--paper); font-family: "Arimo", Arial, sans-serif; color: var(--ink); }
  .letterhead { position: relative; width: 950px; height: 1200px; background: var(--paper); }

  .brand-square { position: absolute; left: 127px; top: 3px; width: 70px; height: 56px; background: var(--navy); }
  .brand-name {
    position: absolute; left: 70px; top: 132px; width: 200px;
    font-size: 19px; line-height: 22px; font-weight: 400; color: var(--navy);
    letter-spacing: 0.5px; text-align: center;
  }

  .recipient { position: absolute; left: 76px; top: 339px; font-size: 14.5px; line-height: 16px; }
  .salutation { position: absolute; left: 78px; top: 466px; font-size: 15.5px; font-weight: 700; }

  .body-copy { position: absolute; left: 78px; top: 527px; width: 790px; font-size: 14px; line-height: 16px; }
  .body-copy p { margin-bottom: 16px; }

  .signatory { position: absolute; left: 82px; top: 860px; }
  .signatory-name { font-size: 18.5px; font-weight: 700; line-height: 22px; }
  .signatory-role { font-size: 17px; line-height: 22px; }
  .signature { position: absolute; left: 77px; top: 926px; width: 150px; height: 70px;
    background: linear-gradient(90deg, rgba(12,23,41,0.18), rgba(12,23,41,0.08)); }

  .footer-rule { position: absolute; left: 84px; top: 1041px; width: 38px; height: 3px; background: var(--rule); }
  .footer-contact { position: absolute; left: 84px; top: 1061px; font-size: 13px; line-height: 17px; }
  .footer-contact .address { margin-bottom: 9px; }
  .contact-line { display: flex; align-items: center; gap: 8px; height: 16px; }
  .contact-line svg { width: 11px; height: 11px; fill: var(--navy); flex: none; }
</style>
</head>
<body>
<main class="letterhead">
  <div class="brand-square"></div>
  <div class="brand-name">TELLWICK ASSET<br>MANAGEMENT</div>

  <address class="recipient" style="font-style: normal;">
    Mr Daniel Harrow<br>
    Founder and CEO<br>
    Your Company,<br>
    412 Alderbrook Lane, Suite 210<br>
    Ridgeford, Canada 58210
  </address>

  <p class="salutation">Dear Sir</p>

  <section class="body-copy">
    <p>Lorem ipsum dolor sit amet. Non quam iste ut dolor repellendus aut quasi porro nam molestias ullam ut sint ipsa! Qui accusamus assumenda qui quae tempore sit quia velit aut porro tempora. Est iste explicabo aut alias impedit est sequi quis.</p>
    <p>Cum rerum molestiae id galisum odit et autem voluptas aut blanditiis iste ut aspernatur itaque ut tempora laudantium vel voluptatem repudiandae! Ea delectus omnis est voluptas odit ut assumenda quisquam eos facere sunt qui quis vitae. Qui velit dolorem in distinctio</p>
    <p>dignissimos rem voluptatem totam ut quia nostrum cum quas consequuntur. Quo aliquid earum eum optio ducimus qui fugiat veniam qui blanditiis velit ut quos dolores non officiis enim ut voluptatem veritatis.</p>
    <p>At quia sunt nam quibusdam mollitia aut rerum laudantium et inventore molestiae aut cumque consequatur. 33 minima velit rem quasi galisum ut quae magni sed praesentium possimus 33 commodi quam qui quae aperiam est enim accusantium. Sed Quis laboriosam ut suscipit maxime cum reprehenderit adipisci. Non nihil dolor ut obcaecati commodi aut Quis provident eos doloribus cumque.</p>
    <p>At quia sunt nam quibusdam mollitia aut rerum laudantium et inventore molestiae aut cumque consequatur. 33 minima velit rem quasi galisum ut quae</p>
  </section>

  <div class="signatory">
    <div class="signatory-name">PETER VANCE</div>
    <div class="signatory-role">President</div>
  </div>
  <div class="signature" role="img" aria-label="Handwritten signature of Peter Vance"></div>

  <div class="footer-rule"></div>
  <div class="footer-contact">
    <div class="address">412 Alderbrook Lane<br>Ridgeford, Canada 58210</div>
    <div class="contact-line">
      <svg viewBox="0 0 24 24" aria-hidden="true"><path d="M6.6 10.8a15.1 15.1 0 0 0 6.6 6.6l2.2-2.2a1 1 0 0 1 1-.25 11.4 11.4 0 0 0 3.6.57 1 1 0 0 1 1 1V20a1 1 0 0 1-1 1A17 17 0 0 1 3 4a1 1 0 0 1 1-1h3.5a1 1 0 0 1 1 1c0 1.25.2 2.45.57 3.57a1 1 0 0 1-.25 1z"/></svg>
      <span>555-014-2387</span>
    </div>
    <div class="contact-line">
      <svg viewBox="0 0 24 24" aria-hidden="true"><path d="M2 5h20v14H2z M2 5l10 8 10-8" fill="none" stroke="#0c1729" stroke-width="0"/><path d="M2 6.5V19h20V6.5l-10 7.5z M2.8 5h18.4L12 12z"/></svg>
      <span>info@tellwickasset.example</span>
    </div>
  </div>
</main>
</body>
</html>
```